Buch-/E-Book-Cover
Dieser Designer hat seinen Job wirklich makellos erledigt. Er war auch bei der Menge an Anforderungen, die ich an ihn hatte, sehr geduldig und wurde allen Anforderungen mehr als gerecht. Ich wäre sehr erfreut, wenn ich in der Zukunft wieder mit ihm arbeiten kann. Ich sehe eine helle Zukunft für diesen Designer und kann ihn nur jedem weiterempfehlen, der Wert auf sein Produkt legt.
Zielgruppe
Genre: Ratgeber
Autorenname: Malte Osterkamp
Titel: Staatskunde ohne Umwege
Untertitel: Wie Sie endlich mitreden, Ihr Wissen über die deutsche Politik auffrischen und das Land mitgestalten können - Das Politik Buch für Einsteiger
Zielgruppe:
- Personen die Schwierigkeiten haben nachzuvollziehen, was in der Politik geschieht
- Personen die keine Zeit haben, sich durch Nachschlagewerke und co. zu wälzen
- Personen, denen die Wahlentscheidung aufgrund, deren mangelnden Wissens schwer fällt
- Personen, denen das fehlende Wissen über die Politik im Alltag langsam peinlich sind
- Personen, die ihre Meinung in politischen Diskussionen nicht zum Ausdrück bringen können
- Personen, die sich als einzelne machtlos fühlen
- Personen, die mit der politischen Lage unzufrieden sind, jedoch nicht wissen, was wie sein soll
- Personen, die dachten, Politik ist zu langweilig und trocken um sich damit auseinander zu setzen
- Männlich und Weiblich ausgeglichene Zielgruppe
- U.a. junge Leser
Aufgabenstellung
Das ist das Besondere an meinem Buch:
- Die Leser dieses Buches werden in der schnellstmöglichen Zeit ihre politische Unwissenheit besiegen, ohne dass ihnen langweilig wird.
Das sollte meine Leser beim Cover fühlen:
- Sie sollen beim ansehen des Covers das Verlangen verspüren, die Details des Covers erkunden zu wollen.
- Sie sollen sofort erkennen, worum es in dem Buch geht
Das möchte ich besonders hervorheben:
- Ich möchte hervorheben, dass dieses Buch das hochwertigste Buch dieser Thematik ist.
Ich bevorzuge folgende Farben: Helle Farben
Verlagsname und Autorenname dort einfügen wo es am besten passt.
Fonts: Frei Wählbar
Format: Geplant sind 13,34 x 20,32 cm.
Weitere Vorgaben:
- Keine Bilder von echten Personen verwenden
- Seit Kreativ und gestaltet ein ins Auge springendes Cover

```html
<!DOCTYPE html>
<html lang="de">
<head>
<meta charset="utf-8">
<title>Staatskunde ohne Umwege – Buchcover</title>
<link rel="stylesheet" href="https://fonts.googleapis.com/css2?family=Montserrat:wght@500;600;700;800&family=Passion+One&family=Fjalla+One&display=swap">
<style>
  :root {
    --stage: #f3f3f3;
    --signal-red: #f5211f;
    --paper: #ffffff;
    --ink: #1f1f1f;
    --sky-top: #8fb3cf;
    --sky-mid: #d9c7b3;
    --haze: #e7cfb6;
    --roofs: #b4593e;
    --facades: #c9a882;
    --street: #6d6a66;
    --back-shade: rgba(40, 48, 58, 0.55);
    --back-text: #e9ddd0;
  }
  * { box-sizing: border-box; margin: 0; padding: 0; }
  html, body { width: 1200px; height: 824px; overflow: hidden; }
  body {
    background: var(--stage);
    font-family: "Montserrat", sans-serif;
    position: relative;
  }
  .cover {
    position: absolute;
    top: 47px;
    width: 480px;
    height: 730px;
    overflow: hidden;
  }
  .front { left: 110px; }
  .back { left: 620px; }

  .city-photo {
    position: absolute; inset: 0;
    background: linear-gradient(180deg,
      var(--sky-top) 0%, #b7c3cc 22%, var(--sky-mid) 42%, var(--haze) 52%,
      var(--facades) 62%, var(--roofs) 72%, var(--facades) 80%, var(--street) 92%, #55524f 100%);
  }

  /* front */
  .author {
    position: absolute; top: 22px; left: 0; right: 0;
    text-align: center; color: var(--paper);
    font-weight: 700; font-size: 19px; letter-spacing: 5px;
  }
  .author-rule {
    position: absolute; top: 48px; left: 170px; width: 150px; height: 1.5px;
    background: var(--paper);
  }
  .title-band {
    position: absolute; left: 10px; background: var(--paper);
    color: var(--signal-red); font-weight: 800; line-height: 1;
    padding: 0 14px; display: flex; align-items: center;
  }
  .title-band.line-1 { top: 70px; height: 70px; width: 420px; font-size: 43px; }
  .title-band.line-2 { top: 152px; height: 62px; width: 355px; font-size: 39px; }
  .subtitle {
    position: absolute; top: 240px; left: 24px; width: 400px;
    color: var(--ink); font-weight: 600; font-size: 12.2px;
    letter-spacing: 2.1px; line-height: 1.55; text-transform: uppercase;
  }
  .badge {
    position: absolute; left: 258px; top: 330px; width: 170px; height: 150px;
  }
  .badge svg { position: absolute; inset: 0; }
  .badge-text {
    position: absolute; inset: 0; display: flex; align-items: center; justify-content: center;
    text-align: center; color: var(--paper);
    font-family: "Passion One", sans-serif; font-size: 23px; line-height: 1.15; letter-spacing: 0.5px;
  }
  .front-footer {
    position: absolute; left: 0; right: 0; bottom: 0; height: 56px;
    background: var(--signal-red); color: var(--paper);
    display: flex; align-items: center; justify-content: space-between;
    padding: 0 22px 0 48px; font-weight: 700; font-size: 19px; letter-spacing: 5px;
  }

  /* back */
  .back-shade {
    position: absolute; inset: 0;
    background: linear-gradient(180deg, rgba(60,70,82,0.75) 0%, var(--back-shade) 55%, rgba(60,60,60,0.35) 80%);
  }
  .back-title {
    position: absolute; top: 32px; left: 0; right: 0; text-align: center;
    color: var(--paper); font-weight: 800; font-size: 34px; line-height: 1.4;
  }
  .back-tagline {
    position: absolute; top: 138px; left: 32px; color: var(--back-text);
    font-weight: 600; font-size: 12.5px;
  }
  .back-points {
    position: absolute; top: 175px; left: 30px; right: 24px; list-style: none;
    color: var(--back-text); font-weight: 500; font-size: 12.5px; line-height: 1.55;
    text-align: justify;
  }
  .back-points li { margin-bottom: 22px; }
  .back-points li::before { content: "· "; }
  .back-call {
    position: absolute; top: 510px; left: 20px; right: 20px; text-align: center;
    color: var(--paper); font-family: "Fjalla One", sans-serif; font-size: 27px; line-height: 1.25;
  }
  .back-red { position: absolute; left: 0; bottom: 0; width: 480px; height: 150px; }
</style>
</head>
<body>

<section class="cover front" aria-label="Vorderseite">
  <div class="city-photo" role="img" aria-label="Luftaufnahme der Berliner Innenstadt mit Fernsehturm, Dächern und Straße in der Abendsonne"></div>
  <p class="author">MALTE OSTERKAMP</p>
  <div class="author-rule"></div>
  <h1>
    <span class="title-band line-1">STAATSKUNDE</span>
    <span class="title-band line-2">OHNE UMWEGE</span>
  </h1>
  <p class="subtitle">Wie Sie endlich mitreden, Ihr Wissen über die deutsche Politik auffrischen und das Land mitgestalten können</p>
  <div class="badge">
    <svg viewBox="0 0 170 150" aria-hidden="true">
      <path d="M60 6 C110 -4 165 20 168 70 C171 118 130 150 82 146 C34 142 2 118 4 76 C6 40 24 12 60 6 Z" fill="var(--signal-red)"/>
    </svg>
    <p class="badge-text">DAS POLITIK<br>BUCH FÜR<br>EINSTEIGER</p>
  </div>
  <footer class="front-footer"><span>LINDPRESS</span><span>RATGEBER</span></footer>
</section>

<section class="cover back" aria-label="Rückseite">
  <div class="city-photo" role="img" aria-label="Gedämpfte Luftaufnahme der Berliner Innenstadt mit Fernsehturm"></div>
  <div class="back-shade"></div>
  <h2 class="back-title">STAATSKUNDE<br>OHNE UMWEGE</h2>
  <p class="back-tagline">Souverän und sicher durch jedes Politikgespräch</p>
  <ul class="back-points">
    <li>Dank „Staatskunde ohne Umwege“ werden Sie beim Lesen von Nachrichten nicht mehr von Überlegungen abgelenkt, was diese oder jene Begriffe zu bedeuten haben.</li>
    <li>Sie bilden außerdem faktenbasiert eine eigene, gut begründete Meinung und können politische Diskussionen auf Augenhöhe verfolgen und sogar souverän führen.</li>
    <li>Sie erkennen die Probleme der aktuellen Politik und können somit frühzeitig erkennen was für berufliche wie private Folgen auf Ihr Leben haben könnte.</li>
    <li>Mit Ihrem Wissen können Sie andere Menschen aufklären und für die Zusammenhänge der aktuellen Lage begeistern.</li>
  </ul>
  <p class="back-call">Worauf warten Sie noch? Gestalten<br>Sie jetzt unsere Zukunft mit!</p>
  <svg class="back-red" viewBox="0 0 480 150" aria-hidden="true">
    <path d="M0 20 L120 18 L180 26 L230 12 L300 22 L340 10 L380 30 L430 24 L480 40 L480 150 L0 150 Z" fill="var(--signal-red)" opacity="0.85"/>
  </svg>
</section>

</body>
</html>
```